Bourbon whiskey bottle label

I need a bottle label for bourbon whiskey. Size 3" x 5" max. I want design in the label and not a rectangle/square label.

tandrolux = bourbon whiskey = tandro lux

I've attached an example of a label that I really like so maybe this will help inspire.

I'm open to any colors. I want it to stand out. I do like the thought of a white layered background with color design.

I would like it to at least have the following on it:
-tandrolux (logo attached) or just add it yourself
-Private Barrel Select
-Straight Bourbon Whiskey
-Proof (plus little box to write)
-ALC/VOL (plus little box to write)
-Plus an open area (no design) to write message.

bourbon whiskey drinkers and industry

whiskey bourbon, retail

• see project description
• see project description
• see project description

```html
<!DOCTYPE html>
<html lang="en">
<head>
<meta charset="utf-8">
<title>Tandrolux Bourbon Label</title>
<link rel="stylesheet" href="https://fonts.googleapis.com/css2?family=Libre+Baskerville:wght@400&family=Dancing+Script:wght@400&display=swap">
<style>
  :root {
    --page-bg: #f5f5f7;
    --label-paper: #d8d0c0;
    --label-edge: #a08d5c;
    --ink-gold: #a08a45;
    --ink-script: #b3a273;
    --ornament-tone: rgba(160, 138, 69, 0.22);
    --write-box: #eeeeee;
  }
  * { margin: 0; padding: 0; box-sizing: border-box; }
  html, body {
    width: 1200px;
    height: 1073px;
    overflow: hidden;
    background: var(--page-bg);
  }
  .label {
    position: absolute;
    left: 327px;
    top: 49px;
    width: 545px;
    height: 975px;
  }
  .label-shape {
    position: absolute;
    inset: 0;
    width: 100%;
    height: 100%;
  }
  .ornament {
    position: absolute;
    left: 50%;
    transform: translateX(-50%);
    background: var(--ornament-tone);
    border-radius: 24px;
  }
  .ornament-top { top: 100px; width: 420px; height: 44px; }
  .ornament-middle { top: 482px; width: 240px; height: 40px; }
  .ornament-bottom { top: 828px; width: 420px; height: 44px; }
  .brand-name {
    position: absolute;
    top: 162px;
    width: 100%;
    text-align: center;
    font-family: "Libre Baskerville", serif;
    font-weight: 400;
    font-size: 56px;
    letter-spacing: 1px;
    color: var(--ink-gold);
  }
  .barrel-line {
    position: absolute;
    top: 262px;
    width: 100%;
    text-align: center;
    font-family: "Libre Baskerville", serif;
    font-size: 33px;
    letter-spacing: 1px;
    color: var(--ink-gold);
  }
  .style-line {
    position: absolute;
    width: 100%;
    text-align: center;
    font-family: "Dancing Script", cursive;
    color: var(--ink-script);
  }
  .style-straight { top: 308px; font-size: 52px; }
  .style-bourbon { top: 370px; font-size: 66px; }
  .message-area {
    position: absolute;
    top: 540px;
    left: 60px;
    right: 60px;
    height: 200px;
  }
  .strength-row {
    position: absolute;
    top: 760px;
    left: 50px;
    right: 50px;
    display: flex;
    align-items: center;
    justify-content: space-between;
    font-family: "Libre Baskerville", serif;
    font-size: 24px;
    color: var(--ink-script);
  }
  .strength-boxes { display: flex; gap: 38px; }
  .write-box {
    width: 100px;
    height: 52px;
    background: var(--write-box);
  }
</style>
</head>
<body>
  <main class="label">
    <svg class="label-shape" viewBox="0 0 545 975" aria-hidden="true">
      <path d="M20,80 C120,80 180,10 272.5,10 C365,10 425,80 525,80
               C525,95 535,105 545,105 L545,870
               C535,870 525,880 525,895 C425,895 365,965 272.5,965
               C180,965 120,895 20,895 C20,880 10,870 0,870 L0,105
               C10,105 20,95 20,80 Z" fill="var(--label-paper)"/>
      <path d="M30,92 C128,92 184,24 272.5,24 C361,24 417,92 515,92
               C515,104 524,112 532,113 L532,862
               C524,863 515,871 515,883 C417,883 361,951 272.5,951
               C184,951 128,883 30,883 C30,871 21,863 13,862 L13,113
               C21,112 30,104 30,92 Z" fill="none" stroke="var(--label-edge)" stroke-width="3"/>
    </svg>

    <div class="ornament ornament-top" role="img" aria-label="Gold scrollwork flourish"></div>

    <h1 class="brand-name">TANDROLUX</h1>
    <p class="barrel-line">Private Barrel Select</p>
    <p class="style-line style-straight">Straight</p>
    <p class="style-line style-bourbon">Bourbon Whiskey</p>

    <div class="ornament ornament-middle" role="img" aria-label="Small gold scroll divider"></div>

    <div class="message-area" aria-label="Open area for a handwritten message"></div>

    <div class="strength-row">
      <span class="strength-label">Alc/Vol</span>
      <span class="strength-boxes">
        <span class="write-box" aria-label="Box to write alcohol by volume"></span>
        <span class="write-box" aria-label="Box to write proof"></span>
      </span>
      <span class="strength-label">Proof</span>
    </div>

    <div class="ornament ornament-bottom" role="img" aria-label="Gold scrollwork flourish"></div>
  </main>
</body>
</html>
```